Business software developers new website

We need to redesign our website. Our current website is http://www.plumvista.net/index.html, which is outdated and needs a new look. We moved out from web design and have concentrated more on the back end of the systems, for example, system support and security and cloud-based applications. Our major clients include both private and government sectors. We would like to see some designs that are all in one page, simple and clean. Prefer illustrator or obstructed images instead of real-life photos. Must look futuristic yet friendly. Attached the new logo for your references and good luck.

Target Market(s)

Medium to big company for their IT or data management. Either improve or upgrade their current system.

Industry/Entity Type

Business Software

Number of Pages Required

1 page

Colors

Designer to choose colors to be used in the design.

Requirements
Must have
• Simple and clean. Individual assets must be provided in the correct size and format(png or jpeg). Prefer Goggle fonts. Even though the logo color is red, grey and black, still prefer some modern colors that go well with red. When design, must consider the possibility to convert it into responsive.
Nice to have
• White background
Should not have
• real life photos, no slider

```html
<!DOCTYPE html>
<html lang="en">
<head>
<meta charset="utf-8">
<title>PlumVista — Expert Defense For Enterprise</title>
<link rel="stylesheet" href="https://fonts.googleapis.com/css2?family=Raleway:wght@300;400;500;600;700&family=Lato:wght@400;700&display=swap">
<style>
:root{
  --red:#e5242f;
  --ink:#1d1f26;
  --dark:#161a22;
  --footer:#1b1c20;
  --text:#555a64;
  --muted:#8a8f98;
  --line:#dfe2e7;
  --soft:#f3f5f9;
  --white:#ffffff;
}
*{box-sizing:border-box;margin:0;padding:0}
html,body{width:1200px;height:3871px;overflow:hidden}
body{position:relative;background:var(--white);font-family:'Lato',Arial,sans-serif;color:var(--text);font-size:14px;line-height:1.6}
.abs{position:absolute}
h1,h2,h3,h4{font-family:'Raleway',Arial,sans-serif;color:var(--ink);font-weight:400}
.btn{display:inline-flex;align-items:center;justify-content:center;background:var(--red);color:var(--white);font-family:'Raleway',Arial,sans-serif;font-weight:700;font-size:12px;letter-spacing:.5px;border-radius:3px}

/* nav */
.site-nav{left:0;top:0;width:1200px;height:80px;background:var(--white)}
.brand{font-family:'Raleway',Arial,sans-serif;font-weight:600;font-size:28px;color:var(--ink);left:175px;top:20px;display:flex;align-items:center;gap:8px}
.brand-dot{width:10px;height:10px;background:var(--red)}
.menu{left:418px;top:30px;display:flex;gap:26px;font-family:'Raleway',Arial,sans-serif;font-weight:600;font-size:13px;color:var(--ink)}
.nav-call{left:908px;top:20px;width:118px;height:40px}

/* hero */
.hero{left:0;top:80px;width:1200px;height:580px;background:var(--dark);overflow:hidden}
.hero h1{position:absolute;left:175px;top:90px;color:var(--white);font-size:42px;line-height:1.2;font-weight:400}
.hero p{position:absolute;left:175px;top:205px;width:430px;color:#d6d9e0;font-size:14px;line-height:1.5}
.hero .btn{position:absolute;left:175px;top:285px;width:112px;height:42px}
.hero-ask{position:absolute;left:305px;top:295px;color:var(--white);font-size:15px}
.hero-art{position:absolute;left:680px;top:25px;width:430px;height:440px;border-radius:30px;background:linear-gradient(140deg,#3b3fd6 0%,#7b3fe0 45%,#e24a8c 100%);opacity:.9}
.hero-wave{position:absolute;left:0;bottom:0}

/* services */
.section-title{text-align:center;width:1200px;left:0}
.services-title{top:632px;font-size:38px}
.services-sub{top:683px;text-align:center;width:1200px;left:0;font-size:14px;color:var(--text)}
.service{top:805px;width:270px;text-align:center}
.service svg{display:block;margin:0 auto 12px}
.service h3{font-size:15px;font-weight:700;letter-spacing:.3px;margin-bottom:10px}
.service p{font-size:12px;color:var(--muted);line-height:1.6;padding:0 18px}
.services-btn{left:527px;top:990px;width:146px;height:40px}

/* work */
.work-title{top:1200px;font-size:36px;line-height:1.25}
.tabs{left:338px;top:1343px;display:flex;gap:10px}
.tab{height:46px;border:1px solid var(--line);display:flex;align-items:center;justify-content:center;font-family:'Raleway',Arial,sans-serif;font-size:12px;font-weight:600;color:var(--muted)}
.tab.active{background:var(--red);color:var(--white);border-color:var(--red)}
.work-art{left:177px;top:1468px;width:405px;height:245px;border-radius:120px 120px 20px 20px;background:linear-gradient(160deg,#f7e9ee 0%,#e8e9f6 100%)}
.work-copy{left:606px;top:1470px;width:492px;font-size:14px;line-height:1.55}
.work-copy p+p{margin-top:16px}

/* news */
.news-bg{left:0;top:1800px;width:1200px;height:560px;background:var(--soft)}
.news-wave{left:0;top:1800px}
.news-title{top:1860px;font-size:38px}
.news-sub{top:1910px;left:400px;width:400px;text-align:center;font-size:13px;color:var(--muted);line-height:1.4}
.card{top:1984px;width:272px;height:372px;background:var(--white);box-shadow:0 2px 10px rgba(20,30,50,.07)}
.card-art{height:184px;width:100%}
.card-date{position:absolute;left:20px;top:168px;height:26px;padding:0 12px;background:var(--red);color:var(--white);font-size:11px;font-weight:700;display:flex;align-items:center;gap:6px}
.card-body{padding:34px 20px 0}
.card-by{font-size:12px;color:var(--muted)}
.card-by b{color:var(--red);font-weight:700}
.card h3{font-size:15px;font-weight:600;margin:6px 0 8px}
.card p{font-size:12px;color:var(--muted);line-height:1.5}
.card-more{margin-top:10px;font-size:12px;font-weight:700;color:var(--red)}

/* testimonials */
.say-title{top:2478px;font-size:38px}
.say-sub{top:2528px;left:400px;width:400px;text-align:center;font-size:13px;color:var(--muted);line-height:1.4}
.say-art{left:150px;top:2560px;width:335px;height:310px;border-radius:16px;background:linear-gradient(150deg,#e4f2fb 0%,#cfe6f5 100%)}
.quote-box{left:516px;top:2581px;width:516px;height:258px;background:#f4f4f5;padding:76px 60px 0;text-align:center}
.quote-mark{position:absolute;left:50%;top:12px;transform:translateX(-50%);font-family:'Raleway',Arial,sans-serif;font-size:90px;line-height:1;color:#c9ccd2}
.quote-box p{font-size:12px;color:var(--muted);line-height:1.6}
.quote-box h4{margin-top:22px;font-size:14px;font-weight:700}

/* contact */
.contact-bg{left:0;top:2936px;width:1200px;height:554px;background:#f2f3f6}
.contact-title{left:175px;top:2995px;font-size:38px;color:var(--ink)}
.contact-sub{left:175px;top:3050px;width:420px;font-size:13px;color:var(--muted);line-height:1.45}
.field{background:var(--white);border:1px solid var(--line);font-size:13px;color:var(--text);padding:0 14px;display:flex;align-items:center}
.field.area{align-items:flex-start;padding-top:12px}
.send{left:175px;top:3348px;width:416px;height:44px}
.contact-art{left:660px;top:2965px;width:400px;height:500px;border-radius:20px;background:linear-gradient(160deg,#e5eef8 0%,#d6e4f1 100%)}

/* footer */
.footer{left:0;top:3490px;width:1200px;height:381px;background:var(--footer);color:#c7cad1}
.footer .brand{color:var(--white);left:175px;top:58px}
.footer-about{left:175px;top:112px;width:250px;font-size:12px;line-height:1.55;color:#c7cad1}
.footer-contact{left:175px;top:193px;font-size:12px;line-height:2}
.footer-contact div{display:flex;align-items:center;gap:8px}
.footer h4{color:var(--white);font-size:14px;font-weight:700}
.links{left:474px;top:62px}
.links ul{list-style:none;margin-top:18px;font-size:12px;line-height:1.9}
.links li::before{content:"";display:inline-block;width:4px;height:4px;background:var(--red);margin-right:8px;vertical-align:middle}
.signup{left:612px;top:62px;width:190px}
.signup .field{margin-top:18px;height:34px;background:transparent;border-color:#4a4d55;color:#c7cad1;font-size:12px}
.signup .btn{margin-top:10px;width:190px;height:34px}
.locate{left:832px;top:62px}
.map{margin-top:20px;width:200px;height:92px;background:linear-gradient(135deg,#e9ece6,#d9dfe6)}
.footer-bar{left:175px;top:318px;width:857px;border-top:1px solid #33353c;padding-top:20px;display:flex;justify-content:space-between;font-size:11px;color:#9aa0aa}
.social{display:flex;gap:10px;margin-top:-4px}
.social span{width:24px;height:24px;border-radius:50%;border:1px solid #4a4d55;display:block}
</style>
</head>
<body>

<header class="site-nav abs">
  <div class="brand abs">plumvista.net<span class="brand-dot"></span></div>
  <nav class="menu abs"><span>HOME</span><span>OUR SERVICES</span><span>FAQ</span><span>NEWS</span><span>OUR CLIENTS</span><span>CONTACT</span></nav>
  <span class="btn nav-call abs">CALL NOW</span>
</header>

<section class="hero abs">
  <h1>Expert Defense<br>For Enterprise</h1>
  <p>Plumvista is an Australian based Software and Web Development Company that provides individual technology solutions and professional software for clients worldwide.</p>
  <span class="btn">READ MORE</span>
  <span class="hero-ask">Questions? Talk to our team</span>
  <div class="hero-art" role="img" aria-label="Isometric illustration of a large screen with charts and small figures working on data"></div>
  <svg class="hero-wave" width="1200" height="130" viewBox="0 0 1200 130">
    <path d="M0 70 C220 140 420 130 620 80 C820 30 1000 10 1200 60 L1200 130 L0 130 Z" fill="#ffffff"/>
  </svg>
</section>

<h2 class="section-title services-title abs">Our Services</h2>
<div class="services-sub abs">We are Experts in Security &amp; Cloud-Based Applications</div>

<div class="service abs" style="left:178px">
  <svg width="46" height="40" viewBox="0 0 46 40" fill="none" stroke="#1d1f26" stroke-width="2"><rect x="3" y="3" width="40" height="26" rx="2"/><path d="M16 37h14M23 29v8"/><path d="M14 20l6-7 5 5 7-8" stroke="#e5242f"/></svg>
  <h3>SYSTEM SUPPORT</h3>
  <p>Contrary to popular belief, our support team keeps every system running smoothly around the clock.</p>
</div>
<div class="service abs" style="left:465px">
  <svg width="46" height="40" viewBox="0 0 46 40" fill="none" stroke="#1d1f26" stroke-width="2"><rect x="3" y="3" width="40" height="30" rx="2"/><path d="M23 9l9 4v6c0 5-4 8-9 10-5-2-9-5-9-10v-6z" stroke="#e5242f"/></svg>
  <h3>SECURITY</h3>
  <p>Contrary to popular belief, strong security starts with careful audits and layered defenses.</p>
</div>
<div class="service abs" style="left:755px">
  <svg width="46" height="40" viewBox="0 0 46 40" fill="none" stroke="#1d1f26" stroke-width="2"><path d="M12 30a8 8 0 0 1 1-16 11 11 0 0 1 21 3 7 7 0 0 1 0 13z"/><path d="M23 34V20m-5 5l5-5 5 5" stroke="#e5242f"/></svg>
  <h3>CLOUD-BASED APPLICATIONS</h3>
  <p>Contrary to popular belief, cloud apps can scale with your business without extra hardware.</p>
</div>
<span class="btn services-btn abs">VIEW ALL SERVICES</span>

<h2 class="section-title work-title abs">Our work is based on quality sales,<br>customer and technical support services</h2>
<div class="tabs abs">
  <div class="tab active" style="width:194px">ABOUT US</div>
  <div class="tab" style="width:116px">PHILOSOPHY</div>
  <div class="tab" style="width:148px">FAQ</div>
</div>
<div class="work-art abs" role="img" aria-label="Illustration of a team reading a large book together"></div>
<div class="work-copy abs">
  <p>Our work is based on quality sales, customer and technical support services.<br>Being oriented towards innovative products in our work, we come up with essential tools for online business enhancing. Our programming specialists focus on delivering solutions for small start-ups as well as large organizations and companies. The team of purposeful and experienced professionals works hard to extract maximum performance from modern information technologies.</p>
  <p>Providing the best quality of service and excellence of support we established a global presence in the software market. Our clients come from all over the world.</p>
</div>

<div class="news-bg abs"></div>
<svg class="news-wave abs" width="1200" height="90" viewBox="0 0 1200 90">
  <path d="M0 0 L0 30 C120 -10 240 70 380 40 C430 30 450 0 470 0 Z" fill="#ffffff"/>
</svg>
<h2 class="section-title news-title abs">News</h2>
<div class="news-sub abs">Lorem ipsum dolor sit amet, consectetur adipiscing elit, sed do eiusmod tempor incididunt ut labore et dolore magna aliqua.</div>

<article class="card abs" style="left:177px">
  <div class="card-art" role="img" aria-label="Illustration of a desk with planning boards" style="background:linear-gradient(135deg,#4fa3d9,#f2a23b)"></div>
  <div class="card-date">May 16, 2019</div>
  <div class="card-body">
    <div class="card-by">By: <b>Owen</b></div>
    <h3>Sed ut perspiciatis unde omnis iste</h3>
    <p>Lorem ipsum is filler text that shows how a short news excerpt fits in this card layout.</p>
    <div class="card-more">Read More &gt;&gt;</div>
  </div>
</article>
<article class="card abs" style="left:461px">
  <div class="card-art" role="img" aria-label="Illustration of a person at a large screen" style="background:linear-gradient(135deg,#5a3fb8,#8a55d6)"></div>
  <div class="card-date">April 3, 2019</div>
  <div class="card-body">
    <div class="card-by">By: <b>Reyes</b></div>
    <h3>Nemo enim ipsam voluptatem quia</h3>
    <p>Lorem ipsum is filler text that shows how a short news excerpt fits in this card layout.</p>
    <div class="card-more">Read More &gt;&gt;</div>
  </div>
</article>
<article class="card abs" style="left:761px">
  <div class="card-art" role="img" aria-label="Illustration of a team around a web dashboard" style="background:linear-gradient(135deg,#f5d63a,#3f8ee0)"></div>
  <div class="card-date">May 8, 2019</div>
  <div class="card-body">
    <div class="card-by">By: <b>Hale</b></div>
    <h3>Quis autem vel eum iure reprehe</h3>
    <p>Lorem ipsum is filler text that shows how a short news excerpt fits in this card layout.</p>
    <div class="card-more">Read More &gt;&gt;</div>
  </div>
</article>

<h2 class="section-title say-title abs">What Users Saying</h2>
<div class="say-sub abs">Lorem ipsum dolor sit amet, consectetur adipiscing elit, sed do eiusmod tempor incididunt ut labore et dolore magna aliqua.</div>
<div class="say-art abs" role="img" aria-label="Illustration of people analysing charts on a board"></div>
<div class="quote-box abs">
  <span class="quote-mark">&#8220;</span>
  <p>Quis ipsum suspendisse ultrices gravida. Risus commodo viverra maecenas accumsan lacus vel facilisis. Lorem ipsum dolor sit amet, consectetur adipiscing elit, sed do eiusmod tempor incididunt ut labore et dolore magna aliqua.</p>
  <h4>Mara Ellison</h4>
</div>

<div class="contact-bg abs"></div>
<h2 class="contact-title abs">Any question? Ask us</h2>
<div class="contact-sub abs">Lorem ipsum dolor sit amet, consectetur adipiscing elit, sed do eiusmod tempor incididunt ut labore et dolore magna aliqua.</div>
<div class="field abs" style="left:175px;top:3120px;width:183px;height:40px">Name*</div>
<div class="field abs" style="left:388px;top:3120px;width:203px;height:40px">Email*</div>
<div class="field abs" style="left:175px;top:3176px;width:416px;height:40px;justify-content:space-between">Subject<svg width="10" height="6" viewBox="0 0 10 6"><path d="M0 0h10L5 6z" fill="#555a64"/></svg></div>
<div class="field area abs" style="left:175px;top:3232px;width:416px;height:100px">Talk to us</div>
<span class="btn send abs">SEND</span>
<div class="contact-art abs" role="img" aria-label="Illustration of a person beside a large stack of web pages and a plant"></div>

<footer class="footer abs">
  <div class="brand abs">plumvista.net<span class="brand-dot"></span></div>
  <p class="footer-about abs">We have provided web design, graphic design and application development solutions for a wide variety of industries [...]</p>
  <div class="footer-contact abs">
    <div><svg width="12" height="12" viewBox="0 0 12 12"><path d="M2 1l2 0 1 3-1.5 1a7 7 0 0 0 3.5 3.5L8 7l3 1v2a1 1 0 0 1-1 1A9 9 0 0 1 1 2a1 1 0 0 1 1-1z" fill="#e5242f"/></svg>+61 7 5550 0142</div>
    <div><svg width="12" height="10" viewBox="0 0 12 10"><rect width="12" height="10" rx="1" fill="#e5242f"/><path d="M1 1l5 4 5-4" stroke="#1b1c20" fill="none"/></svg>support@plumvista.net</div>
  </div>
  <div class="links abs">
    <h4>Quick links</h4>
    <ul><li>Home</li><li>Our Services</li><li>Our Clients</li><li>Contact</li></ul>
  </div>
  <div class="signup abs">
    <h4>Signup For newsletter</h4>
    <div class="field">Email</div>
    <span class="btn">SUBSCRIBE</span>
  </div>
  <div class="locate abs">
    <h4>Locate Us</h4>
    <div class="map" role="img" aria-label="Street map showing the office location"></div>
  </div>
  <div class="footer-bar abs">
    <span>© 2019 copyright PlumVista. All rights reserved</span>
    <div class="social"><span></span><span></span><span></span></div>
  </div>
</footer>

</body>
</html>
```